Crestline Lending Group Business Cards

We are looking to revamp the current business cards each of our locations uses. We are a lending company that specializes in personal loans, title loans, and tax services. We have locations in New Mexico, Texas, and Oklahoma.

We would like a cleaner, sleeker look while still highlighting what we offer. Title Loans, Personal Loans & Tax Services. We also want to include our referral fee somewhere on the card. We would like to see an English option as well as a Spanish option for the cards.

PLEASE NOTE: Some business cards do not include the employee's name but just the store's location, while others will include both.

These are double-sided business cards, and we would like to see proof if possible. I have included proofs of our current business cards for you to review below, as well as our company logo. Feel free to get creative with the logo, etc! Colors should match the logo; however, you do not need to use all of our logo colors if you don't want to.

```html
<!DOCTYPE html>
<html lang="en">
<head>
<meta charset="utf-8">
<title>Crestline Lending Group – Business Cards</title>
<link href="https://fonts.googleapis.com/css2?family=Montserrat:wght@300;400;500;700;800&display=swap" rel="stylesheet">
<style>
  :root {
    --green: #0f5a2e;
    --red: #c8202f;
    --ink: #1c1c1c;
    --paper: #f4f4f4;
    --backdrop: #dcdcdc;
  }
  * { margin: 0; padding: 0; box-sizing: border-box; }
  html, body { width: 1200px; height: 802px; overflow: hidden; }
  body {
    background: var(--backdrop);
    font-family: "Montserrat", Arial, sans-serif;
    position: relative;
    color: var(--ink);
  }
  .card {
    position: absolute;
    background: var(--paper);
    box-shadow: 0 6px 18px rgba(0,0,0,0.18);
    overflow: hidden;
  }

  /* Front: portrait referral card */
  .card-front { left: 120px; top: 140px; width: 300px; height: 525px; }
  .front-body { position: relative; padding: 40px 26px 0 42px; }
  .accent-line {
    position: absolute; left: 26px; top: 0; width: 3px; height: 150px; background: var(--red);
  }
  .referral-title { color: var(--green); font-weight: 800; font-size: 25px; letter-spacing: 0.5px; line-height: 1.1; }
  .referral-sub { font-weight: 300; font-size: 22px; letter-spacing: 1px; margin-top: 4px; }
  .referral-amount { color: var(--red); font-weight: 800; font-size: 70px; line-height: 1; letter-spacing: -2px; margin-top: 2px; }
  .staff-name { color: var(--green); font-weight: 800; font-size: 27px; margin-top: 34px; line-height: 1; }
  .staff-role { font-size: 15px; margin-top: 4px; }
  .contact-list { list-style: none; margin-top: 14px; font-size: 12.5px; line-height: 1.6; }
  .contact-list li { display: flex; align-items: center; gap: 7px; }
  .contact-list svg { width: 11px; height: 11px; flex: none; }
  .coverage { font-size: 12.5px; margin-top: 10px; }
  .service-list { font-size: 12.5px; font-weight: 500; text-transform: uppercase; margin-top: 14px; line-height: 1.5; text-align: center; margin-left: -16px; }
  .front-band { position: absolute; left: 0; right: 0; bottom: 0; height: 44px; background: var(--green); }

  /* Back: landscape brand card */
  .card-back { left: 480px; top: 230px; width: 600px; height: 343px; }
  .brand-block { position: absolute; left: 0; right: 0; top: 110px; text-align: center; }
  .brand-name {
    display: inline-flex; align-items: center; gap: 12px;
    color: var(--green); font-weight: 700; font-size: 36px;
  }
  .brand-dot { width: 16px; height: 16px; border-radius: 50%; background: var(--red); }
  .brand-web { color: var(--red); font-weight: 500; font-size: 18px; margin-top: 8px; letter-spacing: 0.5px; }
  .brand-services { color: var(--green); font-weight: 500; font-size: 17px; letter-spacing: 1px; margin-top: 44px; }
</style>
</head>
<body>

  <section class="card card-front">
    <div class="front-body">
      <span class="accent-line"></span>
      <p class="referral-title">REFER A FRIEND</p>
      <p class="referral-sub">GET UP TO</p>
      <p class="referral-amount">$100</p>

      <p class="staff-name">MARIA LOPEZ</p>
      <p class="staff-role">Branch Manager</p>

      <ul class="contact-list">
        <li>
          <svg viewBox="0 0 24 24"><path fill="#1c1c1c" d="M6.6 10.8a15 15 0 0 0 6.6 6.6l2.2-2.2c.3-.3.7-.4 1-.2 1.1.4 2.3.6 3.6.6.6 0 1 .4 1 1V20c0 .6-.4 1-1 1A17 17 0 0 1 3 4c0-.6.4-1 1-1h3.5c.6 0 1 .4 1 1 0 1.3.2 2.5.6 3.6.1.3 0 .7-.2 1z"/></svg>
          (505) 555-0147
        </li>
        <li>
          <svg viewBox="0 0 24 24"><rect x="2" y="5" width="20" height="14" fill="#1c1c1c"/><path d="M2 5l10 8 10-8" fill="none" stroke="#f4f4f4" stroke-width="2"/></svg>
          info@crestlinelending.com
        </li>
        <li>
          <svg viewBox="0 0 24 24" fill="none" stroke="#1c1c1c" stroke-width="2"><circle cx="12" cy="12" r="10"/><path d="M2 12h20M12 2a15 15 0 0 1 0 20M12 2a15 15 0 0 0 0 20"/></svg>
          www.crestlinelending.com
        </li>
      </ul>

      <p class="coverage">New Mexico, Texas, and Oklahoma.</p>
      <p class="service-list">Title Loans | Personal Loans<br>Tax Services</p>
    </div>
    <div class="front-band"></div>
  </section>

  <section class="card card-back">
    <div class="brand-block">
      <p class="brand-name"><span class="brand-dot"></span>Crestline Lending Group</p>
      <p class="brand-web">www.crestlinelending.com</p>
      <p class="brand-services">TITLE LOANS | PERSONAL LOANS | TAX SERVICES</p>
    </div>
  </section>

</body>
</html>
```